Vermilion Reel Works Web Design

COMPANY: VERMILION REEL WORKS
LOCATION: SHANGHAI, CHINA
AREA: FILM/TV DRAMA/COMMERCIALS/GAME POST PRODUCTION, SOUND DESIGN, MUSIC, and GAME.
WEB STYLE: SIMPLE, PROFESSIONAL, TRUSTWORTHY

LANGUAGE: ENGLISH, CHINESE. (Same layout, different language)
UPDATE: AFTER PROJECT FINISHED, WE NEED UPDATE BY OURSELVES.

MAIN SUBJECT: 6
1 HOMEPAGE
2 ABOUT US
3 TEAM
4 SERVICES
5 FACILITY
6 CONTACT

add one page of JOB OPPORTUNITIES.

DETAILS
1 HOMEPAGE
SLOGAN: Vermilion Reel Works provides a well-designed working environment which amplifies your team’s ability to reach their creative goals.

Our services include:
 Feature Films
 Music & Scoring
 Commercials
 ADR & Foley
 Sound & Picture Editorial
 Sound Design
 Video Game

2 ABOUT US
Vermilion Reel Works is located in the premiere South-Bund area of Shanghai. Occupying a 5000 square meter Technical Building, Vermilion Reel Works was built by a filmmaker for filmmakers, and is one of the largest, most versatile full-service post-production facilities in China.

Vermilion Reel Works is positioning to be at the forefront of the latest technology. Our goal is to provide a comprehensive solution for the post-production needs of our clients. We offer two fully-equipped dubbing stages (one of which will be certified KESTRON VOXAR PREMIERE), a large variety of both picture and sound editing rooms, impressive Foley and ADR stages, a world-class scoring stage, and complete audio and video transfer services.

We can handle your entire project from editing all the way to the end of the final sound mix; all under one extremely comfortable roof. We fully realize that the true art is in listening to the needs of our clients and making their greatest vision a reality. To this end our creative team's expertise, with a network of sound supervisors, editors and mixers, will deliver the magic you need. Producers and directors will also find our richly appointed guest accommodations to be a comfortable and soothing place to wind up the day. Every aspect of your project will be taken care of by a skilled and dedicated team, in the way that is best suited to you.

3 TEAM
(attachment 01)

4 SERVICES
Sound Mix
ADR
FOLEY
MUSIC
Sound Design
Sound Edit
Picture Edit
for all the Films, TV Drama, Commercials, Video Games, Online Media
(attachment 02, use photo)

5 FACILITY
(attachment 03)

6 CONTACT
(attachment04)
with map

Project Deadline Extended
Reason: Designers work are great, my bosses will spend 1-2 days select one of these web design, and spend 1-2 days to make some change, maybe use new photos.

```html
<!DOCTYPE html>
<html lang="en">
<head>
<meta charset="utf-8">
<title>Vermilion Reel Works</title>
<link href="https://fonts.googleapis.com/css2?family=Bebas+Neue&display=swap" rel="stylesheet">
<style>
  :root {
    --navy: #14336e;
    --sky: #7fa3ee;
    --white: #ffffff;
    --dark-brown: #2a1d14;
    --band: rgba(30, 24, 20, 0.55);
    --tile: rgba(40, 34, 30, 0.45);
    --tile-line: rgba(235, 235, 235, 0.75);
    --separator: rgba(255, 255, 255, 0.25);
  }
  * { margin: 0; padding: 0; box-sizing: border-box; }
  html, body { width: 1200px; height: 743px; overflow: hidden; }
  body { font-family: "Bebas Neue", "Arial Narrow", sans-serif; color: var(--white); background: #1d1510; }
  .page { position: relative; width: 1200px; height: 743px; overflow: hidden; }
  .hero-photo {
    position: absolute; inset: 0 0 47px 0;
    background:
      radial-gradient(ellipse at 80% 30%, rgba(220, 200, 170, 0.55), transparent 55%),
      radial-gradient(ellipse at 25% 40%, rgba(120, 110, 120, 0.5), transparent 45%),
      linear-gradient(180deg, #7b6a58 0%, #5a4a3c 40%, #2c221b 75%, #1a130e 100%);
  }
  .hero-photo::before { content: ""; position: absolute; left: 0; right: 0; top: 0; height: 3px; background: #b8a68c; }
  .brand {
    position: absolute; left: 120px; top: 9px; width: 139px; height: 61px;
    background: var(--white); display: flex; align-items: center; justify-content: center;
    color: var(--navy); font-size: 19px; letter-spacing: 0.5px; padding-top: 3px;
  }
  .social { position: absolute; top: 9px; left: 980px; display: flex; gap: 6px; }
  .social a {
    width: 32px; height: 32px; border: 1px solid rgba(255,255,255,0.6); border-radius: 3px;
    background: rgba(255,255,255,0.08); display: block;
  }
  .language { position: absolute; right: 0; top: 73px; width: 42px; }
  .language a {
    display: flex; align-items: center; justify-content: center; height: 42px;
    color: var(--white); text-decoration: none; font-size: 17px; padding-top: 2px;
  }
  .language .active { background: var(--navy); }
  .language .other { background: var(--dark-brown); }
  .slogan {
    position: absolute; left: 0; right: 0; top: 251px; height: 180px;
    background: var(--band); text-align: center;
  }
  .slogan-lead { font-size: 28px; margin-top: 22px; line-height: 32px; }
  .slogan-key { font-size: 50px; color: var(--sky); line-height: 52px; margin-top: 4px; }
  .slogan-end { font-size: 28px; line-height: 32px; margin-top: 8px; }
  .services-title { position: absolute; left: 119px; top: 532px; font-size: 25px; }
  .services { position: absolute; left: 120px; top: 568px; display: flex; gap: 10px; list-style: none; }
  .service {
    width: 128px; height: 118px; border: 1px solid var(--tile-line); background: var(--tile);
    display: flex; flex-direction: column; align-items: center; position: relative;
  }
  .service svg { margin-top: 14px; width: 72px; height: 62px; }
  .service-name {
    position: absolute; bottom: 10px; left: 0; right: 0; text-align: center;
    font-size: 14px; line-height: 13px;
  }
  .main-nav {
    position: absolute; left: 0; right: 0; bottom: 0; height: 47px; background: var(--navy);
    display: flex; justify-content: center; align-items: center;
  }
  .main-nav a {
    color: var(--white); text-decoration: none; font-size: 17px; padding: 0 15px; line-height: 26px;
    border-left: 1px solid var(--separator);
  }
  .main-nav a:first-child { border-left: none; }
</style>
</head>
<body>
<div class="page">
  <div class="hero-photo" role="img" aria-label="Sound engineer working at a large mixing console with monitors in a post-production studio"></div>

  <div class="brand">VERMILION REEL WORKS</div>

  <nav class="social" aria-label="Social links">
    <a href="#" aria-label="Social link one"></a>
    <a href="#" aria-label="Social link two"></a>
    <a href="#" aria-label="Social link three"></a>
  </nav>

  <nav class="language" aria-label="Language">
    <a href="#" class="active">EN</a>
    <a href="#" class="other">CH</a>
  </nav>

  <section class="slogan">
    <p class="slogan-lead">Vermilion Reel Works provides a</p>
    <h1 class="slogan-key">Well-designed working environment</h1>
    <p class="slogan-end">which amplifies your team’s ability to reach their creative goals</p>
  </section>

  <h2 class="services-title">Our services include</h2>
  <ul class="services">
    <li class="service">
      <svg viewBox="0 0 72 62" fill="none" stroke="#fff" stroke-width="3">
        <rect x="4" y="6" width="64" height="50"/>
        <rect x="10" y="16" width="24" height="30" fill="#fff" fill-opacity="0.15"/>
        <rect x="38" y="16" width="24" height="30" fill="#fff" fill-opacity="0.15"/>
        <path d="M10 11h4M20 11h4M30 11h4M40 11h4M50 11h4M60 11h4M10 51h4M20 51h4M30 51h4M40 51h4M50 51h4M60 51h4"/>
      </svg>
      <span class="service-name">Feature Films</span>
    </li>
    <li class="service">
      <svg viewBox="0 0 72 62" fill="#fff">
        <path d="M26 12 L58 4 V14 L26 22Z"/>
        <rect x="26" y="12" width="4" height="36"/>
        <rect x="54" y="6" width="4" height="36"/>
        <ellipse cx="22" cy="50" rx="8" ry="6"/>
        <ellipse cx="50" cy="44" rx="8" ry="6"/>
        <path d="M26 26 L58 18 V22 L26 30Z"/>
      </svg>
      <span class="service-name">Music &amp; Scoring</span>
    </li>
    <li class="service">
      <svg viewBox="0 0 72 62" fill="#fff">
        <path d="M26 4 L36 14 L46 4" stroke="#fff" stroke-width="3" fill="none"/>
        <rect x="6" y="14" width="60" height="44" rx="6"/>
        <rect x="12" y="20" width="36" height="32" rx="4" fill="#3a302a"/>
        <circle cx="57" cy="26" r="3" fill="#3a302a"/>
        <circle cx="57" cy="36" r="3" fill="#3a302a"/>
      </svg>
      <span class="service-name">Commercials</span>
    </li>
    <li class="service">
      <svg viewBox="0 0 72 62" fill="none" stroke="#fff" stroke-width="2.5">
        <path d="M12 2v58M29 2v58M45 2v58M62 2v58"/>
        <rect x="7" y="14" width="10" height="14" fill="#3a302a"/>
        <rect x="24" y="26" width="10" height="14" fill="#3a302a"/>
        <rect x="40" y="34" width="10" height="14" fill="#3a302a"/>
        <rect x="57" y="18" width="10" height="14" fill="#3a302a"/>
      </svg>
      <span class="service-name">ADR &amp; Foley</span>
    </li>
    <li class="service">
      <svg viewBox="0 0 72 62" fill="#fff">
        <rect x="10" y="40" width="10" height="3"/><rect x="10" y="46" width="10" height="3"/><rect x="10" y="52" width="10" height="3"/>
        <rect x="23" y="22" width="10" height="3"/><rect x="23" y="28" width="10" height="3"/><rect x="23" y="34" width="10" height="3"/><rect x="23" y="40" width="10" height="3"/><rect x="23" y="46" width="10" height="3"/><rect x="23" y="52" width="10" height="3"/>
        <rect x="36" y="10" width="10" height="3"/><rect x="36" y="16" width="10" height="3"/><rect x="36" y="22" width="10" height="3"/><rect x="36" y="28" width="10" height="3"/><rect x="36" y="34" width="10" height="3"/><rect x="36" y="40" width="10" height="3"/><rect x="36" y="46" width="10" height="3"/><rect x="36" y="52" width="10" height="3"/>
        <rect x="49" y="28" width="10" height="3"/><rect x="49" y="34" width="10" height="3"/><rect x="49" y="40" width="10" height="3"/><rect x="49" y="46" width="10" height="3"/><rect x="49" y="52" width="10" height="3"/>
      </svg>
      <span class="service-name">Sound<br>&amp; Picture Editorial</span>
    </li>
    <li class="service">
      <svg viewBox="0 0 72 62" fill="#fff">
        <path d="M8 22h12l16-14v46L20 40H8z"/>
        <path d="M44 20q6 11 0 22M51 14q10 17 0 34M58 8q14 23 0 46" stroke="#fff" stroke-width="3" fill="none"/>
      </svg>
      <span class="service-name">Sound Design</span>
    </li>
    <li class="service">
      <svg viewBox="0 0 72 62" fill="#fff">
        <circle cx="36" cy="12" r="8"/>
        <rect x="33" y="18" width="6" height="24"/>
        <rect x="12" y="42" width="48" height="14" rx="3"/>
        <rect x="20" y="36" width="10" height="6" rx="2"/>
      </svg>
      <span class="service-name">Video Game</span>
    </li>
  </ul>

  <nav class="main-nav" aria-label="Main">
    <a href="#">Home</a>
    <a href="#">About Us</a>
    <a href="#">Team</a>
    <a href="#">Services</a>
    <a href="#">Facility</a>
    <a href="#">Contact</a>
  </nav>
</div>
</body>
</html>
```